Designing promotion page - poster for Folk High School

I would like a attractive and well-designed page /poster used in a catalogue for the Norwegian Folk High Schools.
The dimensions on the graphical element:
Width: 180 mm
Hight:186 mm
Resolution: min. 450 dpi
This graphical element will be combined with other information about the school, that is static and we cannot change. Please see attachment (“Folk High School – placement of graphic”). The almost square area in the middle of the page iss the one that the designed grapichal element will fill.
A part of completing this, is to hand over the workfile to us in the end when we choose the design (Adobe Photoshop PSD or an InDesign INDD file must be used)
There are also attached some pictures that you are free to use in creating the design as you like. You will choose how many pictures you want to use. Please cut, scale, adjust and sharpen them as you like. Only one requirement: Please use one of the Sri Lanka pictures.
Be creative.
The following text-elements must be used in the page (They are also prioritized – number one means: most important that the reader reads…)
1. Møtet som forandrer --- headline. Yep; needs a font supporting ÆØÅ...
2. Multisport --- different courses we provide at our school.
- Data Media – Japan
- Barn i Fokus
- Helse og Velvære
- Globalt Fokus – Afrika
- Fotball
- Bil og Motor
- Internasjonal
- Worship – Australia
- LYNG-friluft
- Høy Puls
Alle linjer reiser på egne turer i inn –og utland! ---- This should be included as the different courses, but in the bottum of the «box».
3. Spennende fellestur for alle til Sri Lanka ---- Use together with the picture from Sri Lanke (Not too large picture!)
4. Hva skal du bli? ---- small headline.
Vi er gode på veiledning, og hjelper deg med å finne ut hva du skal bli.
5. Flott skole:
- Basseng
- Styrkerom
- Gymsal
- Internatstuer
- Filmsal
- Skolekjøkken
- Verksted
- Fotostudio
- Fitnessrom
_________
The students attending our school is between 18-20 years. Of course, the design and expression must meet their expectations.
Looking forward to see the first drafts!
To understand what this should look like: Check the following link:
https://pagevault.example/trondelsk/docs/trk_hefte__18__web
The poster / graphic we want to create, is similar to the one you find in this brochure from page 20.

```html
<!DOCTYPE html>
<html lang="no">
<head>
<meta charset="utf-8">
<title>Møtet som forandrer</title>
<link rel="stylesheet" href="https://fonts.googleapis.com/css2?family=Arimo:ital,wght@0,700;1,700&family=Roboto+Condensed:ital,wght@0,400;0,700;1,400;1,700&display=swap">
<style>
  :root {
    --teal: #17757f;
    --teal-dark: #0f5f68;
    --teal-text: #1b6f78;
    --yellow: #f6c51a;
    --orange: #ee7a22;
    --paper: #f3f3f3;
    --ink: #2f2f2f;
    --white: #ffffff;
  }
  * { margin: 0; padding: 0; box-sizing: border-box; }
  html, body { width: 1155px; height: 1200px; overflow: hidden; background: var(--paper); }
  .poster { position: relative; width: 1155px; height: 1200px; overflow: hidden; background: var(--paper); font-family: "Roboto Condensed", sans-serif; color: var(--ink); }
  .backdrop { position: absolute; inset: 0; }
  .headline { position: absolute; left: 0; top: 16px; width: 1140px; text-align: center; font-family: "Arimo", sans-serif; font-weight: 700; font-size: 80px; letter-spacing: 0; color: var(--white); }
  .photo { position: absolute; border: 5px solid var(--white); box-shadow: 0 4px 10px rgba(0,0,0,.35); }
  .photo--jump { left: 40px; top: 125px; width: 355px; height: 220px; transform: rotate(7deg); background: linear-gradient(180deg,#9cc3e6 0%,#dbe7f0 60%,#b9aa90 100%); }
  .photo--friends { left: 466px; top: 162px; width: 308px; height: 205px; transform: rotate(-4deg); background: linear-gradient(160deg,#b7bcc0,#4c5968 55%,#2d3b52); }
  .photo--table { left: 25px; top: 373px; width: 308px; height: 212px; transform: rotate(-6deg); background: linear-gradient(140deg,#8aa677,#7f6a7a 50%,#5b6a80); }
  .photo--sunset { left: 158px; top: 573px; width: 322px; height: 132px; transform: rotate(-2deg); background: linear-gradient(180deg,#3e4450 0%,#c98a4a 55%,#3c4a26 100%); }
  .photo--fire { left: 478px; top: 375px; width: 300px; height: 232px; transform: rotate(4deg); background: radial-gradient(circle at 35% 75%,#e98a2c 0,#6b3a2a 18%,#16234e 55%,#1e3580 100%); }
  .photo--beach { left: 306px; top: 268px; width: 224px; height: 224px; border-radius: 50%; background: linear-gradient(180deg,#8cb8e0,#c9d7e2 45%,#a88f7a); }
  .photo--srilanka { left: 608px; top: 788px; width: 504px; height: 344px; border-radius: 50%; border: none; box-shadow: none; transform: rotate(-8deg); background: linear-gradient(180deg,#dcd6c4 0%,#b8b49c 55%,#6f6b4e 80%,#c9c2b0 100%); }
  .tag { position: absolute; }
  .tag__back { position: absolute; inset: 0; background: var(--yellow); transform: skewX(-16deg); }
  .tag__face { position: absolute; left: 12px; top: 10px; right: 16px; bottom: 12px; background: linear-gradient(180deg,#ffffff,#e7e7e7); transform: skewX(-16deg); box-shadow: 0 2px 4px rgba(0,0,0,.25); }
  .tag__label { position: absolute; left: 0; right: 0; top: 50%; transform: translateY(-54%); text-align: center; font-weight: 700; color: var(--teal-text); }
  .tag--multisport { left: 826px; top: 122px; width: 306px; height: 82px; }
  .tag--multisport .tag__label { font-size: 40px; }
  .tag--skole { left: 100px; top: 828px; width: 272px; height: 76px; }
  .tag--skole .tag__label { font-size: 35px; }
  .checklist { position: absolute; list-style: none; }
  .checklist li { display: flex; align-items: center; height: 39.6px; font-size: 33px; }
  .checklist svg { width: 24px; height: 24px; margin-right: 8px; flex: none; }
  .courses { left: 803px; top: 214px; }
  .courses__note { position: absolute; left: 835px; top: 572px; font-style: italic; font-size: 33px; line-height: 40px; }
  .facilities { top: 912px; }
  .facilities li { height: 42.5px; font-size: 35px; }
  .facilities--a { left: 56px; }
  .facilities--b { left: 327px; }
  .guidance { position: absolute; left: 200px; top: 686px; width: 520px; }
  .guidance__title { text-align: right; padding-right: 10px; font-weight: 700; font-style: italic; font-size: 46px; line-height: 52px; color: var(--teal-text); }
  .guidance__text { font-style: italic; font-size: 31px; line-height: 39px; margin-top: 0; }
  .trip { position: absolute; inset: 0; }
</style>
</head>
<body>
<main class="poster">
  <svg class="backdrop" width="1155" height="1200" viewBox="0 0 1155 1200" aria-hidden="true">
    <path d="M0 0H1155V20C900 60 520 120 0 400Z" fill="var(--teal)"/>
    <path d="M1155 20C900 62 520 122 0 400V450C520 150 900 110 1155 70Z" fill="var(--yellow)"/>
    <path d="M1155 70C900 110 520 150 0 450V470C520 175 900 130 1155 95Z" fill="var(--teal-dark)"/>
    <path d="M0 1135C420 1180 820 1010 1155 820V1200H0Z" fill="var(--teal)"/>
    <path d="M0 1172C420 1205 850 1070 1155 950V1010C850 1130 420 1230 0 1200Z" fill="var(--yellow)"/>
    <path d="M280 1200C700 1170 950 1100 1155 1030V1200Z" fill="var(--orange)"/>
  </svg>

  <h1 class="headline">MØTET SOM FORANDRER</h1>

  <div class="photo photo--jump" role="img" aria-label="Photo: four students jumping on a rooftop under blue sky"></div>
  <div class="photo photo--friends" role="img" aria-label="Photo: three students smiling outdoors by rocks"></div>
  <div class="photo photo--table" role="img" aria-label="Photo: students sitting at an outdoor table"></div>
  <div class="photo photo--sunset" role="img" aria-label="Photo: students watching a sunset over grassland"></div>
  <div class="photo photo--fire" role="img" aria-label="Photo: students around a campfire by a lake at dusk"></div>
  <div class="photo photo--beach" role="img" aria-label="Photo: two friends on a beach wearing sunglasses"></div>

  <div class="tag tag--multisport"><div class="tag__back"></div><div class="tag__face"></div><div class="tag__label">MULTISPORT</div></div>

  <ul class="checklist courses">
    <li><svg viewBox="0 0 24 24"><circle cx="11" cy="13" r="9" fill="none" stroke="var(--teal)" stroke-width="2.4"/><path d="M6.5 12.5l4 4L22 4" fill="none" stroke="var(--teal)" stroke-width="2.6"/></svg>Data Media – Japan</li>
    <li><svg viewBox="0 0 24 24"><circle cx="11" cy="13" r="9" fill="none" stroke="var(--teal)" stroke-width="2.4"/><path d="M6.5 12.5l4 4L22 4" fill="none" stroke="var(--teal)" stroke-width="2.6"/></svg>Barn i Fokus</li>
    <li><svg viewBox="0 0 24 24"><circle cx="11" cy="13" r="9" fill="none" stroke="var(--teal)" stroke-width="2.4"/><path d="M6.5 12.5l4 4L22 4" fill="none" stroke="var(--teal)" stroke-width="2.6"/></svg>Helse og Velvære</li>
    <li><svg viewBox="0 0 24 24"><circle cx="11" cy="13" r="9" fill="none" stroke="var(--teal)" stroke-width="2.4"/><path d="M6.5 12.5l4 4L22 4" fill="none" stroke="var(--teal)" stroke-width="2.6"/></svg>Globalt Fokus – Afrika</li>
    <li><svg viewBox="0 0 24 24"><circle cx="11" cy="13" r="9" fill="none" stroke="var(--teal)" stroke-width="2.4"/><path d="M6.5 12.5l4 4L22 4" fill="none" stroke="var(--teal)" stroke-width="2.6"/></svg>Fotball</li>
    <li><svg viewBox="0 0 24 24"><circle cx="11" cy="13" r="9" fill="none" stroke="var(--teal)" stroke-width="2.4"/><path d="M6.5 12.5l4 4L22 4" fill="none" stroke="var(--teal)" stroke-width="2.6"/></svg>Bil og Motor</li>
    <li><svg viewBox="0 0 24 24"><circle cx="11" cy="13" r="9" fill="none" stroke="var(--teal)" stroke-width="2.4"/><path d="M6.5 12.5l4 4L22 4" fill="none" stroke="var(--teal)" stroke-width="2.6"/></svg>Internasjonal</li>
    <li><svg viewBox="0 0 24 24"><circle cx="11" cy="13" r="9" fill="none" stroke="var(--teal)" stroke-width="2.4"/><path d="M6.5 12.5l4 4L22 4" fill="none" stroke="var(--teal)" stroke-width="2.6"/></svg>Worship – Australia</li>
    <li><svg viewBox="0 0 24 24"><circle cx="11" cy="13" r="9" fill="none" stroke="var(--teal)" stroke-width="2.4"/><path d="M6.5 12.5l4 4L22 4" fill="none" stroke="var(--teal)" stroke-width="2.6"/></svg>LYNG-friluft</li>
  </ul>
  <p class="courses__note">Alle linjer reiser på egne<br>turer i inn –og utland!</p>

  <section class="guidance">
    <h2 class="guidance__title">Hva skal du bli?</h2>
    <p class="guidance__text">Vi er gode på veiledning, og hjelper<br>deg med å finne ut hva du skal bli.</p>
  </section>

  <div class="tag tag--skole"><div class="tag__back"></div><div class="tag__face"></div><div class="tag__label">FLOTT SKOLE</div></div>

  <ul class="checklist facilities facilities--a">
    <li><svg viewBox="0 0 24 24"><circle cx="11" cy="13" r="9" fill="none" stroke="var(--teal)" stroke-width="2.4"/><path d="M6.5 12.5l4 4L22 4" fill="none" stroke="var(--teal)" stroke-width="2.6"/></svg>Basseng</li>
    <li><svg viewBox="0 0 24 24"><circle cx="11" cy="13" r="9" fill="none" stroke="var(--teal)" stroke-width="2.4"/><path d="M6.5 12.5l4 4L22 4" fill="none" stroke="var(--teal)" stroke-width="2.6"/></svg>Styrkerom</li>
    <li><svg viewBox="0 0 24 24"><circle cx="11" cy="13" r="9" fill="none" stroke="var(--teal)" stroke-width="2.4"/><path d="M6.5 12.5l4 4L22 4" fill="none" stroke="var(--teal)" stroke-width="2.6"/></svg>Gymsal</li>
    <li><svg viewBox="0 0 24 24"><circle cx="11" cy="13" r="9" fill="none" stroke="var(--teal)" stroke-width="2.4"/><path d="M6.5 12.5l4 4L22 4" fill="none" stroke="var(--teal)" stroke-width="2.6"/></svg>Internatstuer</li>
    <li><svg viewBox="0 0 24 24"><circle cx="11" cy="13" r="9" fill="none" stroke="var(--teal)" stroke-width="2.4"/><path d="M6.5 12.5l4 4L22 4" fill="none" stroke="var(--teal)" stroke-width="2.6"/></svg>Filmsal</li>
  </ul>
  <ul class="checklist facilities facilities--b">
    <li><svg viewBox="0 0 24 24"><circle cx="11" cy="13" r="9" fill="none" stroke="var(--teal)" stroke-width="2.4"/><path d="M6.5 12.5l4 4L22 4" fill="none" stroke="var(--teal)" stroke-width="2.6"/></svg>Skolekjøkken</li>
    <li><svg viewBox="0 0 24 24"><circle cx="11" cy="13" r="9" fill="none" stroke="var(--teal)" stroke-width="2.4"/><path d="M6.5 12.5l4 4L22 4" fill="none" stroke="var(--teal)" stroke-width="2.6"/></svg>Verksted</li>
    <li><svg viewBox="0 0 24 24"><circle cx="11" cy="13" r="9" fill="none" stroke="var(--teal)" stroke-width="2.4"/><path d="M6.5 12.5l4 4L22 4" fill="none" stroke="var(--teal)" stroke-width="2.6"/></svg>Fotostudio</li>
    <li><svg viewBox="0 0 24 24"><circle cx="11" cy="13" r="9" fill="none" stroke="var(--teal)" stroke-width="2.4"/><path d="M6.5 12.5l4 4L22 4" fill="none" stroke="var(--teal)" stroke-width="2.6"/></svg>Fitnessrom</li>
  </ul>

  <div class="photo photo--srilanka" role="img" aria-label="Photo: stilt fishermen on poles by the sea in Sri Lanka"></div>

  <svg class="trip" width="1155" height="1200" viewBox="0 0 1155 1200">
    <defs><path id="trip-arc" d="M582 962C590 828 722 702 900 702C1012 702 1100 762 1152 845"/></defs>
    <text font-family="Arimo, sans-serif" font-weight="700" font-size="34" fill="var(--orange)">
      <textPath href="#trip-arc" textLength="722" lengthAdjust="spacing">Spennende fellestur for alle til Sri Lanka</textPath>
    </text>
  </svg>
</main>
</body>
</html>
```